Create an app design

Design a very simple travel app with the following specifications

Sign up/login page
- Username
- Phone number

Password code
- Type in 4 codes sent to your phone

Home page
- List of places friends have posted they're traveling to

Friends
- List of friends and where they're currently located
- Follow people by searching or adding from contact

Search
- Search for a specific country, state, or country and get a list of the people you follow who are there

```html
<!DOCTYPE html>
<html lang="en">
<head>
<meta charset="utf-8">
<title>Simple travel app – layout</title>
<link href="https://fonts.googleapis.com/css2?family=Nunito:wght@400;600;700;800&family=Yellowtail&display=swap" rel="stylesheet">
<style>
:root{
  --page:#f1f1f3;
  --card:#ffffff;
  --blue:#3b30f2;
  --blue-text:#3a34d8;
  --accent-line:#5a6ae6;
  --ink:#222230;
  --muted:#8a8a96;
  --field:#f3f3f5;
  --divider:#ececf0;
}
*{box-sizing:border-box;margin:0;padding:0}
html,body{width:1200px;height:2719px;overflow:hidden}
body{background:var(--page);position:relative;font-family:"Nunito",sans-serif;color:var(--ink)}
.board-title{position:absolute;left:157px;top:150px;width:466px;text-align:center;white-space:nowrap;font-family:"Yellowtail",cursive;font-weight:400;font-size:70px;color:var(--blue-text);line-height:1;z-index:2}
.board-rule{position:absolute;left:131px;top:294px;width:446px;height:5px;background:var(--accent-line)}
.board-note{position:absolute;left:131px;top:340px;width:466px;text-align:center;font-size:33px;letter-spacing:-.5px;color:#1d1d24}

.screen{position:absolute;width:345px;background:var(--card);border-radius:14px;overflow:hidden;box-shadow:0 28px 30px -22px rgba(0,0,0,.28)}
.screen.intro{background:linear-gradient(#f6f6f8 0%,#fff 45%)}
.screen > *{position:absolute}
.wordmark{left:0;width:100%;text-align:center;font-size:48px;font-weight:800;color:var(--blue)}
.field-label{left:33px;font-size:17px;color:#2a2a33}
.field-label small{font-size:8px;color:var(--muted)}
.field{left:31px;width:285px;height:48px;background:var(--field);border-radius:4px;font-size:11px;color:#c4c4cc;padding:16px 20px}
.btn{left:31px;width:285px;height:48px;background:var(--blue);border-radius:5px;color:#fff;font-size:16px;font-weight:600;display:flex;align-items:center;justify-content:center}
.code-box{top:550px;width:57px;height:49px;background:var(--field);border-radius:3px}
.code-heading{left:31px;top:508px;font-size:22px;font-weight:600;color:#2a2a33}
.sparkle{border-radius:50%;background:#7f8ff0}

.status{top:8px;left:14px;right:14px;display:flex;justify-content:space-between;align-items:center;font-size:12px;font-weight:700}
.screen-title{left:31px;top:48px;font-size:31px;font-weight:700;color:var(--blue-text);letter-spacing:-.5px}
.header-icon{right:26px;top:60px}
.photo{border-radius:50%}
.person-name{font-size:17px;font-weight:600;letter-spacing:-.3px}
.person-place{font-size:15px;color:#444;display:flex;align-items:center;gap:4px;margin-top:4px}
.person{display:flex;align-items:center;gap:20px;left:41px}
.person .photo{width:64px;height:64px;flex:none}

.section-label{left:34px;top:118px;font-size:19px;color:#333}
.view-all{right:16px;top:126px;font-size:11px;color:#aaa}
.avatar-row{display:flex;gap:7px;left:32px}
.avatar-row .photo{width:45px;height:45px;flex:none}
.place{left:32px;font-size:15px;font-weight:600;color:var(--blue-text);display:flex;align-items:center;gap:6px}
.post-image{left:32px;width:295px;height:173px;border-radius:2px}
.post-caption{position:absolute;left:10px;bottom:16px;color:#fff}
.post-caption b{display:block;font-size:20px;line-height:1.15;font-weight:800}
.post-caption span{display:block;font-size:9px;margin-top:3px}
.post-dots{position:absolute;left:18px;top:8px;color:#fff;font-size:20px;letter-spacing:1px;line-height:1}
.divider{left:0;right:0;height:2px;background:var(--divider)}

.search-field{left:31px;top:104px;width:284px;height:48px;background:var(--field);border-radius:4px;font-size:11px;color:#c4c4cc;padding:16px 20px}
.filter{left:35px;top:160px;font-size:17px;color:var(--blue-text);display:flex;align-items:center;gap:6px}
.dest{top:203px;width:92px}
.dest .dest-image{height:157px;border-radius:2px}
.dest b{display:block;font-size:15px;font-weight:700;margin-top:6px;line-height:1}
.dest span{display:block;font-size:8px;color:#aaa}
.subheading{left:35px;top:424px;font-size:21px;color:var(--blue-text)}
.search .person{left:35px;gap:20px}
.search .person .photo{width:62px;height:62px}
</style>
</head>
<body>

<h1 class="board-title">Simple travel app</h1>
<div class="board-rule"></div>
<p class="board-note">This is just the layout design</p>

<!-- Sign up -->
<section class="screen intro" style="left:181px;top:480px;height:747px">
  <div class="wordmark" style="top:190px">Logo</div>
  <label class="field-label" style="top:368px">User Name</label>
  <div class="field" style="top:395px">Enter your full name</div>
  <label class="field-label" style="top:452px">Mobile Number</label>
  <div class="field" style="top:479px">Enter Your Phone number</div>
  <label class="field-label" style="top:535px">Email <small>(Optional)</small></label>
  <div class="field" style="top:560px">Enter Your Email</div>
  <div class="btn" style="top:624px">Next</div>
</section>

<!-- Code -->
<section class="screen intro" style="left:704px;top:149px;height:747px">
  <span class="sparkle" style="left:90px;top:162px;width:4px;height:4px"></span>
  <span class="sparkle" style="left:250px;top:168px;width:5px;height:5px"></span>
  <span class="sparkle" style="left:217px;top:150px;width:3px;height:3px;background:#cfd6f5"></span>
  <svg style="left:273px;top:180px" width="16" height="12" viewBox="0 0 16 12"><path d="M2 6l4 4 8-8" fill="none" stroke="#9fd9b8" stroke-width="2"/></svg>
  <div class="wordmark" style="top:210px">Logo</div>
  <div class="code-heading">Enter your code</div>
  <div class="code-box" style="left:37px"></div>
  <div class="code-box" style="left:109px"></div>
  <div class="code-box" style="left:183px"></div>
  <div class="code-box" style="left:255px;width:52px"></div>
  <div class="btn" style="top:612px">Proceed</div>
</section>

<!-- Friends -->
<section class="screen" style="left:704px;top:991px;height:745px">
  <div class="status"><span>9:41</span>
    <svg width="54" height="12" viewBox="0 0 54 12"><rect x="0" y="8" width="3" height="4" fill="#111"/><rect x="4" y="6" width="3" height="6" fill="#111"/><rect x="8" y="3" width="3" height="9" fill="#111"/><path d="M18 5a9 9 0 0 1 12 0M21 8a5 5 0 0 1 6 0" stroke="#111" stroke-width="2" fill="none"/><circle cx="24" cy="11" r="1.3" fill="#111"/><rect x="34" y="2" width="18" height="9" rx="2" fill="#111"/></svg>
  </div>
  <h2 class="screen-title">Friends</h2>
  <svg class="header-icon" width="24" height="18" viewBox="0 0 24 18"><path d="M23 9H2M9 2L2 9l7 7" fill="none" stroke="var(--blue)" stroke-width="2"/></svg>
  <div role="img" aria-label="Illustration of a person beside a large contact list screen" style="left:83px;top:133px;width:180px;height:76px;background:linear-gradient(90deg,#6a5ce8 0 22%,#eef0fb 22% 88%,#4aa56e 88%);border-radius:4px"></div>
  <div class="btn" style="left:73px;top:236px;width:196px;height:37px;font-size:15px">Import from contacts</div>

  <div class="person" style="top:306px"><div class="photo" role="img" aria-label="Portrait photo of a friend" style="background:#8a6a58"></div><div><div class="person-name">Tomas Ruvell</div><div class="person-place"><svg width="10" height="14" viewBox="0 0 10 14"><path d="M5 0a5 5 0 0 1 5 5c0 4-5 9-5 9S0 9 0 5a5 5 0 0 1 5-5z" fill="var(--blue)"/><circle cx="5" cy="5" r="2" fill="#fff"/></svg>Mexico City</div></div></div>
  <div class="person" style="top:386px"><div class="photo" role="img" aria-label="Portrait photo of a friend" style="background:#c46a4a"></div><div><div class="person-name">Alina Brecker</div><div class="person-place"><svg width="10" height="14" viewBox="0 0 10 14"><path d="M5 0a5 5 0 0 1 5 5c0 4-5 9-5 9S0 9 0 5a5 5 0 0 1 5-5z" fill="var(--blue)"/><circle cx="5" cy="5" r="2" fill="#fff"/></svg>Fes</div></div></div>
  <div class="person" style="top:470px"><div class="photo" role="img" aria-label="Portrait photo of a friend" style="background:#c9a46e"></div><div><div class="person-name">Mara Lindqvist</div><div class="person-place"><svg width="10" height="14" viewBox="0 0 10 14"><path d="M5 0a5 5 0 0 1 5 5c0 4-5 9-5 9S0 9 0 5a5 5 0 0 1 5-5z" fill="var(--blue)"/><circle cx="5" cy="5" r="2" fill="#fff"/></svg>Amsterdam</div></div></div>
  <div class="person" style="top:554px"><div class="photo" role="img" aria-label="Portrait photo of a friend" style="background:#2f3433"></div><div><div class="person-name">Oren Castell</div><div class="person-place"><svg width="10" height="14" viewBox="0 0 10 14"><path d="M5 0a5 5 0 0 1 5 5c0 4-5 9-5 9S0 9 0 5a5 5 0 0 1 5-5z" fill="var(--blue)"/><circle cx="5" cy="5" r="2" fill="#fff"/></svg>Siena</div></div></div>
  <div class="person" style="top:637px"><div class="photo" role="img" aria-label="Portrait photo of a friend" style="background:#3a2c28"></div><div><div class="person-name">Felix Dunmore</div><div class="person-place"><svg width="10" height="14" viewBox="0 0 10 14"><path d="M5 0a5 5 0 0 1 5 5c0 4-5 9-5 9S0 9 0 5a5 5 0 0 1 5-5z" fill="var(--blue)"/><circle cx="5" cy="5" r="2" fill="#fff"/></svg>Singapore</div></div></div>
</section>

<!-- Home -->
<section class="screen" style="left:181px;top:1351px;height:1157px">
  <div class="status"><span>9:41</span>
    <svg width="54" height="12" viewBox="0 0 54 12"><rect x="0" y="8" width="3" height="4" fill="#111"/><rect x="4" y="6" width="3" height="6" fill="#111"/><rect x="8" y="3" width="3" height="9" fill="#111"/><path d="M18 5a9 9 0 0 1 12 0M21 8a5 5 0 0 1 6 0" stroke="#111" stroke-width="2" fill="none"/><circle cx="24" cy="11" r="1.3" fill="#111"/><rect x="34" y="2" width="18" height="9" rx="2" fill="#111"/></svg>
  </div>
  <h2 class="screen-title">Home</h2>
  <svg class="header-icon" width="28" height="28" viewBox="0 0 28 28"><circle cx="12" cy="12" r="10" fill="none" stroke="var(--blue)" stroke-width="2.4"/><path d="M19.5 19.5L26 26" stroke="var(--blue)" stroke-width="2.4"/></svg>
  <div class="section-label">Friends</div>
  <div class="view-all">View All</div>
  <div class="avatar-row" style="top:150px;gap:7px">
    <div class="photo" role="img" aria-label="Friend photo" style="width:53px;height:53px;background:#b98a7a"></div>
    <div class="photo" role="img" aria-label="Friend photo" style="width:53px;height:53px;background:#a86a5a"></div>
    <div class="photo" role="img" aria-label="Friend photo" style="width:53px;height:53px;background:#5a4a3c"></div>
    <div class="photo" role="img" aria-label="Friend photo" style="width:53px;height:53px;background:#2c3552"></div>
    <div class="photo" role="img" aria-label="Friend photo" style="width:53px;height:53px;background:#7a5646"></div>
    <div class="photo" role="img" aria-label="Friend photo" style="width:53px;height:53px;background:#3c3634"></div>
  </div>

  <div class="place" style="top:232px"><svg width="11" height="15" viewBox="0 0 10 14"><path d="M5 0a5 5 0 0 1 5 5c0 4-5 9-5 9S0 9 0 5a5 5 0 0 1 5-5z" fill="var(--blue)"/><circle cx="5" cy="5" r="2" fill="#fff"/></svg>Copenhagen, Denmark</div>
  <div class="post-image" role="img" aria-label="Photo of a Copenhagen harbour with colourful houses and boats" style="top:264px;background:linear-gradient(160deg,#c9c4bc,#8d7a68 55%,#5a5048)">
    <span class="post-dots">•••</span>
    <div class="post-caption"><b>My First Visit<br>to Copenhagen</b><span>Copenhagen, Denmark<br>2019/12/01</span></div>
  </div>
  <div class="avatar-row" style="top:446px">
    <div class="photo" role="img" aria-label="Friend photo" style="background:#8a5a44"></div>
    <div class="photo" role="img" aria-label="Friend photo" style="background:#4a3a34"></div>
    <div class="photo" role="img" aria-label="Friend photo" style="background:#a97a62"></div>
    <div class="photo" role="img" aria-label="Friend photo" style="background:#c4664a"></div>
    <div class="photo" role="img" aria-label="Friend photo" style="background:#9a8478"></div>
  </div>
  <div class="divider" style="top:513px"></div>

  <div class="place" style="top:532px"><svg width="11" height="15" viewBox="0 0 10 14"><path d="M5 0a5 5 0 0 1 5 5c0 4-5 9-5 9S0 9 0 5a5 5 0 0 1 5-5z" fill="var(--blue)"/><circle cx="5" cy="5" r="2" fill="#fff"/></svg>Madrid, Spain</div>
  <div class="post-image" role="img" aria-label="Photo of a seaside marina with white buildings" style="top:564px;background:linear-gradient(#2e5f9c,#5f8fb8 50%,#2a7f8a)">
    <span class="post-dots">•••</span>
    <div class="post-caption"><b>Best of Madrid<br>in Two Days</b><span>Madrid, Spain<br>2019/12/01</span></div>
  </div>
  <div class="avatar-row" style="top:746px">
    <div class="photo" role="img" aria-label="Friend photo" style="background:#d9a070"></div>
    <div class="photo" role="img" aria-label="Friend photo" style="background:#8c7c74"></div>
    <div class="photo" role="img" aria-label="Friend photo" style="background:#6a4a3a"></div>
  </div>
  <div class="divider" style="top:813px"></div>

  <div class="place" style="top:832px"><svg width="11" height="15" viewBox="0 0 10 14"><path d="M5 0a5 5 0 0 1 5 5c0 4-5 9-5 9S0 9 0 5a5 5 0 0 1 5-5z" fill="var(--blue)"/><circle cx="5" cy="5" r="2" fill="#fff"/></svg>Marrakesh, Morocco</div>
  <div class="post-image" role="img" aria-label="Photo of a traveller under a stone arch overlooking a tower" style="top:864px;background:linear-gradient(90deg,#6a5e58,#8fb3d4 45%,#c9a07a 70%,#6a5e58)">
    <span class="post-dots">•••</span>
    <div class="post-caption"><b>Spending time<br>in Marrakech</b><span>Marrakech, Morocco<br>2019/12/01</span></div>
  </div>
  <div class="avatar-row" style="top:1046px">
    <div class="photo" role="img" aria-label="Friend photo" style="background:#b07a5a"></div>
    <div class="photo" role="img" aria-label="Friend photo" style="background:#9fb7c4"></div>
    <div class="photo" role="img" aria-label="Friend photo" style="background:#c48a70"></div>
    <div class="photo" role="img" aria-label="Friend photo" style="background:#7a6a5a"></div>
    <div class="photo" role="img" aria-label="Friend photo" style="background:#5a3a2c"></div>
  </div>
  <div class="divider" style="top:1113px"></div>
</section>

<!-- Search -->
<section class="screen search" style="left:705px;top:1820px;height:747px">
  <div class="status"><span>9:41</span>
    <svg width="54" height="12" viewBox="0 0 54 12"><rect x="0" y="8" width="3" height="4" fill="#111"/><rect x="4" y="6" width="3" height="6" fill="#111"/><rect x="8" y="3" width="3" height="9" fill="#111"/><path d="M18 5a9 9 0 0 1 12 0M21 8a5 5 0 0 1 6 0" stroke="#111" stroke-width="2" fill="none"/><circle cx="24" cy="11" r="1.3" fill="#111"/><rect x="34" y="2" width="18" height="9" rx="2" fill="#111"/></svg>
  </div>
  <h2 class="screen-title">Search</h2>
  <svg class="header-icon" width="24" height="18" viewBox="0 0 24 18"><path d="M23 9H2M9 2L2 9l7 7" fill="none" stroke="var(--blue)" stroke-width="2"/></svg>
  <div class="search-field">Search
    <svg style="position:absolute;right:18px;top:18px" width="12" height="12" viewBox="0 0 12 12"><circle cx="5" cy="5" r="4" fill="none" stroke="#bbb" stroke-width="1.3"/><path d="M8 8l3 3" stroke="#bbb" stroke-width="1.3"/></svg>
  </div>
  <div class="filter">Filter by <svg width="12" height="8" viewBox="0 0 12 8"><path d="M1 1h10L6 7z" fill="var(--blue)"/></svg></div>
  <div class="dest" style="left:31px"><div class="dest-image" role="img" aria-label="Photo of a city skyline at night beneath a snowy mountain" style="background:linear-gradient(#3a62b0,#7f96c8 40%,#1c2240 60%,#c86a3a)"></div><b>New York</b><span>New York</span></div>
  <div class="dest" style="left:136px"><div class="dest-image" role="img" aria-label="Photo of a city skyline at night beneath a snowy mountain" style="background:linear-gradient(#3a62b0,#7f96c8 40%,#1c2240 60%,#c86a3a)"></div><b>New York</b><span>New York</span></div>
  <div class="dest" style="left:242px"><div class="dest-image" role="img" aria-label="Photo of a city skyline at night beneath a snowy mountain" style="background:linear-gradient(#3a62b0,#7f96c8 40%,#1c2240 60%,#c86a3a)"></div><b>New York</b><span>New York</span></div>
  <div class="subheading">Peoples there</div>

  <div class="person" style="top:485px"><div class="photo" role="img" aria-label="Portrait photo of a followed person" style="background:#8a6a58"></div><div><div class="person-name" style="font-size:16px">Tomas Ruvell</div><div class="person-place"><svg width="10" height="14" viewBox="0 0 10 14"><path d="M5 0a5 5 0 0 1 5 5c0 4-5 9-5 9S0 9 0 5a5 5 0 0 1 5-5z" fill="var(--blue)"/><circle cx="5" cy="5" r="2" fill="#fff"/></svg>Mexico City</div></div></div>
  <div class="person" style="top:561px"><div class="photo" role="img" aria-label="Portrait photo of a followed person" style="background:#c46a4a"></div><div><div class="person-name" style="font-size:16px">Alina Brecker</div><div class="person-place"><svg width="10" height="14" viewBox="0 0 10 14"><path d="M5 0a5 5 0 0 1 5 5c0 4-5 9-5 9S0 9 0 5a5 5 0 0 1 5-5z" fill="var(--blue)"/><circle cx="5" cy="5" r="2" fill="#fff"/></svg>Fes</div></div></div>
  <div class="person" style="top:638px"><div class="photo" role="img" aria-label="Portrait photo of a followed person" style="background:#c9a46e"></div><div><div class="person-name" style="font-size:16px">Mara Lindqvist</div><div class="person-place"><svg width="10" height="14" viewBox="0 0 10 14"><path d="M5 0a5 5 0 0 1 5 5c0 4-5 9-5 9S0 9 0 5a5 5 0 0 1 5-5z" fill="var(--blue)"/><circle cx="5" cy="5" r="2" fill="#fff"/></svg>Amsterdam</div></div></div>
  <div class="person" style="top:715px;align-items:flex-start"><div class="photo" role="img" aria-label="Portrait photo of a followed person" style="background:#2f3433"></div><div><div class="person-name" style="font-size:16px;margin-top:-4px">Oren Castell</div></div></div>
</section>

</body>
</html>
```